Quillex Landing Page & Logo

We are building a landing page for a new blockchain-based project called Quillex. The site should look modern and minimalistic with a very brief description of the upcoming project ("Unlock your Brevitan governance stack. Win weekly prizes and a quarterly jackpot!"), a viper logo (the animal - but can just be lettering) , and a button to subscribe for updates and early access.
Examples of similar pages:
https://pondru.finance/
https://www.zentrimo.org/
https://lumbrecks.com/
https://q8.io/
https://www.tovern.finance/
Crypto Users (Specifically Brevitan holders)

```html
<!DOCTYPE html>
<html lang="en">
<head>
<meta charset="utf-8">
<title>Quillex — Landing Page</title>
<link href="https://fonts.googleapis.com/css2?family=Saira+Condensed:wght@700;800&family=Heebo:wght@400;500;700&display=swap" rel="stylesheet">
<style>
  :root {
    --bg: #02071a;
    --bg-card: #050d26;
    --mint: #6ac9a8;
    --mint-soft: #2f9e82;
    --mint-deep: #0f3f3a;
    --navy-btn: #0a1a45;
    --white: #ffffff;
    --red: #e0102b;
    --tile: #ffffff;
    --tile-ink: #3a3f47;
    --tile-muted: #7a808a;
  }
  * { box-sizing: border-box; margin: 0; padding: 0; }
  html, body { width: 670px; height: 1200px; overflow: hidden; background: var(--bg); }
  body { font-family: "Heebo", Arial, sans-serif; font-weight: 400; color: var(--white); }
  .page { position: relative; width: 670px; height: 1200px; overflow: hidden;
    background:
      radial-gradient(ellipse 420px 120px at 335px 1110px, rgba(40,90,110,.3), transparent 70%),
      radial-gradient(ellipse 380px 60px at 335px 625px, rgba(25,182,196,.14), transparent 75%),
      var(--bg); }
  .abs { position: absolute; }
  .display { font-family: "Saira Condensed", "Arial Narrow", sans-serif; font-weight: 800; text-transform: uppercase; }

  /* header */
  .menu-btn { left: 75px; top: 10px; width: 16px; height: 15px; background: var(--navy-btn); border-radius: 3px; display: flex; flex-direction: column; justify-content: center; align-items: center; gap: 1.5px; }
  .menu-btn span { width: 6px; height: 1.2px; background: var(--white); display: block; }
  .brand { left: 0; width: 670px; text-align: center; }
  .brand-top { top: 2px; }
  .brand-name { font-size: 24px; line-height: 24px; color: var(--white); letter-spacing: .3px; }
  .brand-tag { font-family: "Heebo", Arial, sans-serif; font-weight: 400; font-size: 5.5px; letter-spacing: .1px; margin-top: 3px; }
  .pill { top: 8px; height: 18px; width: 54px; border-radius: 9px; font-size: 9px; line-height: 18px; text-align: center; }
  .pill-doc { left: 483px; background: var(--mint); color: var(--navy-btn); }
  .pill-app { left: 543px; background: var(--navy-btn); color: var(--white); }

  /* hero */
  .hero-art { left: 165px; top: 100px; width: 330px; height: 260px; border-radius: 8px;
    background: linear-gradient(160deg, var(--mint-deep) 0%, var(--mint-soft) 45%, var(--mint) 60%, var(--mint-deep) 100%); opacity: .9; }

  /* section heads */
  .section-title { left: 0; width: 670px; text-align: center; font-size: 25px; line-height: 26px; letter-spacing: .2px; text-shadow: 1px 1px 0 var(--red); }

  /* project cards */
  .card { top: 429px; width: 164px; height: 204px; background: var(--bg-card); border-radius: 6px; padding: 4px; text-align: center; }
  .card-media { width: 156px; height: 113px; border-radius: 6px; }
  .media-1 { background: linear-gradient(135deg, #0d2a36, #1d5a66 50%, #0a1f2b); }
  .media-2 { background: linear-gradient(135deg, #0f4a4e, #2fb3a6 55%, #0c3b40); }
  .media-3 { background: linear-gradient(160deg, #1ac4d8, #3fe3e0 50%, #1b9bc8); }
  .card-title { font-size: 7.4px; line-height: 10.5px; margin: 11px 2px 2px; letter-spacing: 0; }
  .card-text { font-size: 6px; line-height: 10.5px; margin: 0 3px; }

  /* investors */
  .tile { width: 102px; height: 46px; background: var(--tile); border-radius: 3px; display: flex; flex-direction: column; align-items: center; justify-content: center; color: var(--tile-ink); }
  .tile-mark { width: 12px; height: 12px; background: var(--tile-ink); margin-bottom: 3px; }
  .tile-mark.round { border-radius: 50%; }
  .tile-name { font-weight: 700; font-size: 8px; line-height: 9px; letter-spacing: .4px; text-transform: uppercase; }
  .tile-tag { font-size: 2.6px; letter-spacing: .3px; text-transform: uppercase; color: var(--tile-muted); margin-top: 1px; }

  /* subscribe */
  .field { top: 981px; width: 161px; height: 27px; border: 1px solid var(--white); border-radius: 3px; font-size: 5.8px; line-height: 25px; padding-left: 7px; }
  .submit { left: 300px; top: 1029px; width: 70px; height: 20px; background: var(--white); border-radius: 3px; box-shadow: 0 1px 0 var(--red); color: var(--navy-btn); font-size: 8.5px; line-height: 20px; text-align: center; }

  /* footer */
  .brand-foot { top: 1075px; }
  .brand-foot .brand-name { font-size: 32px; line-height: 32px; }
  .brand-foot .brand-tag { font-size: 7.4px; margin-top: 3px; }
  .legal { left: 0; top: 1130px; width: 670px; text-align: center; font-size: 5.6px; }
  .socials { left: 0; top: 1147px; width: 670px; display: flex; justify-content: center; gap: 7px; }
  .social { width: 21px; height: 21px; border: 1px solid var(--mint); border-radius: 50%; font-size: 4.6px; line-height: 19px; text-align: center; color: var(--mint); }
</style>
</head>
<body>
<main class="page">

  <header>
    <div class="abs menu-btn" aria-label="Menu"><span></span><span></span><span></span></div>
    <div class="abs brand brand-top">
      <div class="brand-name display">Quillex</div>
      <div class="brand-tag">UNLOCK YOUR GOVERANCE BREVs. WIN BIG.</div>
    </div>
    <div class="abs pill pill-doc display">Doc</div>
    <div class="abs pill pill-app display">App</div>
  </header>

  <section class="hero">
    <div class="abs hero-art" role="img" aria-label="Isometric illustration of mint server towers linked by thin lines to three coin platforms"></div>
  </section>

  <h2 class="abs section-title display" style="top:390px;">Upcoming Project</h2>

  <section class="projects">
    <article class="abs card" style="left:74px;">
      <div class="card-media media-1" role="img" aria-label="Glowing blockchain cubes in dark space"></div>
      <h3 class="card-title display">Lorem ipsum dolor sit amet consectetur adipiscing elit sed do eiusmod.</h3>
      <p class="card-text">Lorem ipsum dolor sit amet, consectetur adipiscing elit, sed do eiusmod tempor incididunt ut labore et dolore magna aliqua.</p>
    </article>
    <article class="abs card" style="left:253px;">
      <div class="card-media media-2" role="img" aria-label="Teal wireframe chain links"></div>
      <h3 class="card-title display">Lorem ipsum dolor sit amet consectetur adipiscing elit sed do eiusmod.</h3>
      <p class="card-text">Lorem ipsum dolor sit amet, consectetur adipiscing elit, sed do eiusmod tempor incididunt ut labore et dolore magna aliqua.</p>
    </article>
    <article class="abs card" style="left:432px;">
      <div class="card-media media-3" role="img" aria-label="Isometric city of data buildings on cyan ground"></div>
      <h3 class="card-title display">Lorem ipsum dolor sit amet consectetur adipiscing elit sed do eiusmod.</h3>
      <p class="card-text">Lorem ipsum dolor sit amet, consectetur adipiscing elit, sed do eiusmod tempor incididunt ut labore et dolore magna aliqua.</p>
    </article>
  </section>

  <h2 class="abs section-title display" style="top:707px;">Our Investors</h2>

  <section class="investors">
    <div class="abs tile" style="left:87px;top:758px;"><div class="tile-mark"></div><div class="tile-name">Nodekra</div><div class="tile-tag">seed partner</div></div>
    <div class="abs tile" style="left:218px;top:765px;"><div class="tile-mark round"></div><div class="tile-name">Syntaro</div><div class="tile-tag">seed partner</div></div>
    <div class="abs tile" style="left:350px;top:758px;"><div class="tile-mark"></div><div class="tile-name">Veltrix</div><div class="tile-tag">core backer</div></div>
    <div class="abs tile" style="left:481px;top:765px;"><div class="tile-mark round"></div><div class="tile-name">Orbelle</div><div class="tile-tag">core backer</div></div>
    <div class="abs tile" style="left:87px;top:821px;"><div class="tile-mark"></div><div class="tile-name">Compuvo</div><div class="tile-tag">early fund</div></div>
    <div class="abs tile" style="left:218px;top:828px;"><div class="tile-mark round"></div><div class="tile-name">Namora</div><div class="tile-tag">early fund</div></div>
    <div class="abs tile" style="left:350px;top:821px;"><div class="tile-mark"></div><div class="tile-name">Lumora</div><div class="tile-tag">growth ally</div></div>
    <div class="abs tile" style="left:481px;top:828px;"><div class="tile-mark round"></div><div class="tile-name">Arctek</div><div class="tile-tag">growth ally</div></div>
  </section>

  <h2 class="abs section-title display" style="top:943px;">Subscribe for Updates</h2>

  <form class="subscribe">
    <div class="abs field" style="left:171px;">Name</div>
    <div class="abs field" style="left:338px;">Email Address</div>
    <div class="abs submit display">Subscribe</div>
  </form>

  <footer>
    <div class="abs brand brand-foot">
      <div class="brand-name display">Quillex</div>
      <div class="brand-tag">UNLOCK YOUR GOVERANCE BREVs. WIN BIG.</div>
    </div>
    <p class="abs legal">© copyrights 2022 Quillex &nbsp;| &nbsp;&nbsp; All rights reserved.</p>
    <nav class="abs socials">
      <div class="social">Socly</div>
      <div class="social">Chirpo</div>
      <div class="social">Vidra</div>
    </nav>
  </footer>

</main>
</body>
</html>
```